Website Design for a Graphic Design Studio in California

We are working with a graphic design company in California.
PLEASE NOTE: We report and ban any designer that reaches out directly to our customers.

Some sites to use for content/competitors and inspiration:

http://quelvint.co.uk
https://www.fendro.studio
https://www.zuplo.io (Client's Favorite)
https://www.merigoldcrafts.com
https://craftwimble.com
https://www.dravinsultonmask.com/us/home/

Thank you for taking the time to consider designing a website for us. We are web developers based in Stockton, CA, USA. Most of our projects go through the same process. Understanding this process may help you win a project with us. We custom-code all of our websites in-house. We don’t have any requirements as to what tools you use for your design, but we prefer Figma files. For any design that we label as four-stars, we send it to the client for review. The client picks the final design they want us to use. Once we complete this process, we will continue to show additional clients all the four-star sites and purchase them later. Your designs will have multiple chances to sell. For better chances of success, we ask that you follow these guidelines.

IMAGES:
If you use any images or icons in the design, we ask that you have a link to the asset so we can purchase the image/icon. Most of the designs we submit do not have the customer’s images on them unless they have some great images. Be creative; show us the feeling you are trying to portray with your image choices. Use any royalty-free site you choose. We subscribe to Tessaly and mainly use their images, but we can purchase images outside of Tessaly. PLEASE NOTE: we will not submit designs to clients with watermarks on the images.

FONTS:
We ask that you identify the fonts used in the design. This can be done in a message if you want. We typically use Brindle Fonts and Tessaly Fonts.

CONTENT:
We're always open to different content and ideas. We often submit designs with stock images so the client can see our vision. We typically take pictures after the website launch to use their images with our vision. Lorem Ipsum is fine for paragraphs, but we ask that you write the headers in correct English. We want to be able to show the vision and identify the sections of the website.

INSPIRATION:
We typically add a couple of links in the brief of websites we like to help you get started in your design.

REVISIONS:
We do not often ask for revisions of the designs unless we see something in the design that may not appeal to the client. If there are slight changes that we want to make, we do that in the development process.

FEEDBACK:
We rarely give feedback on designs during the design process. We are working on many website projects and do not have the time to provide feedback. We usually respond if your request is well thought out and asks specific questions, but a note asking “feedback, please” usually goes unanswered.

```html
<!DOCTYPE html>
<html lang="en">
<head>
<meta charset="utf-8">
<title>Verantis Creative – Mobile View</title>
<link rel="stylesheet" href="https://fonts.googleapis.com/css2?family=Cinzel:wght@400;500&family=DM+Sans:wght@400;500&display=swap">
<style>
:root{
  --gold:#D8A54E;
  --ink:#151515;
  --white:#FFFFFF;
  --dark-text:#222222;
  --rule:#E2BE7A;
  --serif:"Cinzel", "Trajan Pro", serif;
  --sans:"DM Sans", Arial, sans-serif;
}
*{margin:0;padding:0;box-sizing:border-box}
html,body{width:1200px;height:1200px;overflow:hidden}
body{background:var(--gold);position:relative;font-family:var(--serif)}
.screen{position:absolute;overflow:hidden;border:2px solid var(--ink);border-radius:26px}
.screen--dark{background:var(--ink);color:var(--white)}
.screen--light{background:var(--white);color:var(--dark-text)}
.screen--gold{background:var(--gold);color:var(--dark-text)}

/* top-left: about */
.about{left:245px;top:-30px;width:310px;height:243px}
.about__text{position:absolute;left:14px;top:52px;font-size:16px;line-height:21px;letter-spacing:.4px;white-space:nowrap}
.about__strip{position:absolute;left:0;bottom:0;width:100%;height:16px;background:linear-gradient(90deg,#3a2e22,#6b5640,#2b2b2b)}

/* hero */
.hero{left:226px;top:222px;width:350px;height:757px;background:var(--ink)}
.hero__photo{position:absolute;left:0;top:0;width:100%;height:708px;background:linear-gradient(160deg,#2d2f33 0%,#3b3d42 30%,#6d5a36 55%,#2f3135 80%,#1f2023 100%)}
.hero__brand{position:absolute;left:24px;top:28px;display:flex;align-items:center;gap:8px;font-size:15px;letter-spacing:1px;color:var(--white)}
.hero__brand-dot{width:22px;height:22px;border:2px solid var(--white);border-radius:50%}
.hero__brand small{display:block;font-size:7px;letter-spacing:2px;line-height:8px}
.hero__menu{position:absolute;right:12px;top:32px}
.hero__title{position:absolute;left:19px;top:158px;font-size:44px;line-height:51px;font-weight:400;color:var(--white);white-space:nowrap}
.hero__lead{position:absolute;right:12px;top:456px;width:340px;text-align:right;font-size:18.5px;line-height:24px;color:var(--white);white-space:nowrap}

/* bottom-left: signage */
.signage{left:246px;top:985px;width:310px;height:260px}
.signage__photo{position:absolute;left:26px;top:15px;width:268px;height:166px;background:linear-gradient(120deg,#4a3f34,#8a6f4c 45%,#2e2b28)}
.signage__tag{position:absolute;left:8px;top:180px;transform:rotate(-90deg);transform-origin:0 0;font-family:var(--sans);font-size:8px;white-space:nowrap;color:var(--white)}

/* top-right: contact */
.contact{left:687px;top:-30px;width:309px;height:186px}
.contact__title{position:absolute;left:14px;top:48px;font-size:21.5px;line-height:26px;font-weight:400;white-space:nowrap}
.contact__rule{position:absolute;left:14px;top:155px;width:246px;height:2px;background:var(--rule)}
.contact__text{position:absolute;left:14px;top:172px;font-family:var(--sans);font-size:11px;text-decoration:underline;white-space:nowrap}

/* right: guide */
.guide{left:687px;top:215px;width:309px;height:670px}
.guide__title{position:absolute;left:14px;top:22px;font-size:29.5px;line-height:35px;font-weight:400;white-space:nowrap}
.guide__text{position:absolute;left:14px;top:130px;font-family:var(--sans);font-size:12px;line-height:20.2px;letter-spacing:-.2px;white-space:nowrap}
.guide__button{position:absolute;left:14px;top:358px;width:132px;height:34px;border-radius:17px;background:var(--white);font-family:var(--sans);font-size:10px;display:flex;align-items:center;justify-content:center}
.guide__photo{position:absolute;left:13px;top:451px;width:280px;height:219px;background:linear-gradient(90deg,#c9c6c0,#5f5a52 40%,#2c2b29 70%,#d5d2cc)}

/* bottom-right: propel */
.propel{left:687px;top:943px;width:309px;height:300px}
.propel__title{position:absolute;left:0;top:30px;width:305px;text-align:center;font-size:21px;line-height:24.5px;font-weight:400;white-space:nowrap}
.propel__photo{position:absolute;left:12px;top:155px;width:282px;height:145px;background:linear-gradient(135deg,#e9d9b8,#c8b49a 40%,#6f6459 75%,#3d3733)}

/* brand */
.brand{position:absolute;left:1094px;top:18px}
.brand__dot{position:absolute;left:2px;top:0;width:78px;height:78px;border:7px solid var(--white);border-radius:50%}
.brand__name{position:absolute;left:84px;top:110px;transform:rotate(90deg);transform-origin:0 0;font-size:50px;letter-spacing:7px;color:var(--white);white-space:nowrap;line-height:50px}
.brand__sub{position:absolute;left:30px;top:114px;transform:rotate(90deg);transform-origin:0 0;font-size:25px;letter-spacing:3px;color:var(--white);white-space:nowrap;line-height:25px}

.label{position:absolute;left:18px;top:1168px;transform:rotate(-90deg);transform-origin:0 0;font-size:56px;line-height:56px;color:var(--white);white-space:nowrap}
</style>
</head>
<body>

<section class="screen screen--dark about">
  <p class="about__text">As a full-service branding<br>and package design agency,<br>we know that for your<br>business to thrive, all<br>aspects of your branding &amp;<br>marketing need to work<br>together.</p>
  <div class="about__strip" role="img" aria-label="Photo strip of a studio interior"></div>
</section>

<section class="screen hero">
  <div class="hero__photo" role="img" aria-label="Photo of a modern building facade with gold vertical fins"></div>
  <div class="hero__brand"><span class="hero__brand-dot"></span><span>Verantis<small>Creative</small></span></div>
  <svg class="hero__menu" width="22" height="22" viewBox="0 0 22 22" aria-hidden="true">
    <g fill="var(--white)"><rect x="1" y="2" width="4" height="3"/><rect x="9" y="2" width="4" height="3"/><rect x="17" y="2" width="4" height="3"/><rect x="1" y="10" width="4" height="3"/><rect x="9" y="10" width="4" height="3"/><rect x="17" y="10" width="4" height="3"/><rect x="1" y="18" width="4" height="3"/><rect x="9" y="18" width="4" height="3"/><rect x="17" y="18" width="4" height="3"/></g>
  </svg>
  <h1 class="hero__title">Elevating<br>Brands,<br>Inspiring<br>Stories</h1>
  <p class="hero__lead">We are experts at<br>increasing the value of<br>your brand with<br>imagination, ingenuity and<br>passion.</p>
</section>

<section class="screen screen--dark signage">
  <div class="signage__photo" role="img" aria-label="Photo of a glass storefront with the studio sign"></div>
  <p class="signage__tag">Designing your Tomorrow, today</p>
</section>

<section class="screen screen--light contact">
  <h2 class="contact__title">Want to work with<br>our Verantis<br>Creative branding<br>agency?</h2>
  <div class="contact__rule"></div>
  <p class="contact__text">Sed ut perspiciatis unde omnis iste natus</p>
</section>

<section class="screen screen--gold guide">
  <h2 class="guide__title">The 2024 State of<br>Design Guide is<br>here!</h2>
  <p class="guide__text">Sed ut perspiciatis unde omnis iste natus<br>error sit voluptatem accusantium<br>doloremque laudantium, totam rem<br>aperiam, eaque ipsa quae ab illo<br>inventore veritatis et quasi architecto<br>beatae vitae dicta sunt explicabo. Nemo<br>enim ipsam voluptatem quia voluptas sit<br>aspernatur aut odit aut fugit, sed quia<br>consequuntur magni dolores eos qui<br>ratione voluptatem sequi nesciunt.</p>
  <div class="guide__button">Schedule a Call</div>
  <div class="guide__photo" role="img" aria-label="Photo of a street sign display showing the studio brand"></div>
</section>

<section class="screen screen--dark propel">
  <h2 class="propel__title">How our Verantis<br>Branding Agency Can<br>Propel Your Business<br>Forward</h2>
  <div class="propel__photo" role="img" aria-label="Photo of a team working in a bright studio with sticky notes on the wall"></div>
</section>

<div class="brand">
  <span class="brand__dot"></span>
  <span class="brand__name">Verantis</span>
  <span class="brand__sub">Creative</span>
</div>

<p class="label">Mobile View</p>

</body>
</html>
```